Redesign Canvas Art E-Commerce Website

Help! I hired a couple of companies on Tasklyn.com to build and design an e-commerce website for me. After three long and painful months, I have one that I believe is functional on the back-end, but aesthetically on the front end is a mess.

We are a small family business that will take your digital photo and manipulate it into a digitally created oil, watercolor or impressionist style pieces of artwork that we print on museum quality, gallery grade canvas and ship to the customer, ready to hang.

We are looking to create an e-commerce website where a customer can choose their art style, upload a photo, choose their canvas size and orientation (horizontal or vertical) and checkout. Within 48 hours, we will send them back a proof of their newly created, customized artwork for them to approve or not approve. If they approve, we print, package and ship them the product. If they do not approve, we offer unlimited revisions until they are happy.

As I mentioned, the back end functionality is already there, just need design help. No coding required

Here is a link to the development page that they created: https://brushvellomart.com/development/

As you can see, it looks off...doesnt line up properly, wasted space, weird font. Feel free to either correct the homepage they created or design an entirely new page. I am attaching some examples of before and after photos of artwork for reference. I also think the testimonials page and shop page can use a little style. The content is there and accurate, it just doesn't look pretty. Please keep in mind that our customers will probably not be very tech savvy. The customers will probably be sending us pics of kids, grandkids, pets, family portraits, vacation photos, etc.

Here is one of our competitors - www.pelfandquill.com
Their website looks clean and inviting.

Thank you in advance! Im looking forward to seeing the results. I am including our logo in the attachments (I do not have it in a vector file, just a jpeg)

Target Market(s)

Non tech-savvy indiduals, 30-70 years old

Industry/Entity Type

Please look at https://brushvellomart.com/development/ to see various pages and what the other designers did

Number of Pages Required

1 page

Requirements
Must have
• Verbiage on pages leave "as is" but feel free to change styles. Would like to keep existing four categories on homepage
Nice to have
• Warm and inviting homepage that evokes emotion

```html
<!DOCTYPE html>
<html lang="en">
<head>
<meta charset="utf-8">
<title>Brushvello Creations — Landing Page Design</title>
<link href="https://fonts.googleapis.com/css2?family=Poppins:wght@400;500;600;700&display=swap" rel="stylesheet">
<style>
:root{
  --navy:#0d3b5e;
  --pink:#e5105f;
  --blue:#1a72b8;
  --board:#e0d8d2;
  --tint:#f0f1fd;
  --ink:#1c2b3a;
  --muted:#8a93a0;
  --line:#e3e6ec;
  --gold:#f5b90a;
  --white:#ffffff;
}
*{box-sizing:border-box;margin:0;padding:0}
html,body{width:1200px;height:4194px;overflow:hidden}
body{background:var(--board);font-family:"Poppins",sans-serif;color:var(--ink);position:relative}
.abs{position:absolute}

/* board header */
.board-label{position:absolute;font-size:20px;font-weight:500;color:#3b3b3b}
.board-brand{position:absolute;left:118px;top:108px;font-size:30px;font-weight:600;color:var(--navy);display:flex;align-items:center;gap:10px}
.board-brand .dot{width:22px;height:22px;border-radius:50%;background:var(--pink)}
.swatch{position:absolute;top:86px;width:59px;height:59px;border-radius:50%}
.font-sample{position:absolute;left:882px;font-size:23px;font-weight:600;color:var(--navy);line-height:1}

/* page */
.page{position:absolute;left:244px;top:280px;width:712px;height:3855px;background:var(--white);overflow:hidden}
.topbar{position:absolute;left:0;top:0;width:712px;height:16px;background:var(--navy);color:#fff;font-size:6px;display:flex;align-items:center;padding:0 66px}
.topbar .contact{display:flex;gap:16px;align-items:center}
.topbar .auth{margin-left:auto}
.nav{position:absolute;top:16px;left:0;width:712px;height:42px;border-bottom:1px solid var(--line);display:flex;align-items:center;padding:0 68px}
.logo{font-size:14px;font-weight:600;color:var(--navy);display:flex;align-items:center;gap:5px}
.logo .mark{width:10px;height:10px;border-radius:50%;background:var(--pink)}
.nav ul{list-style:none;display:flex;gap:14px;margin-left:auto;font-size:6.5px;font-weight:500;color:var(--muted)}
.nav ul li.active{color:var(--pink)}
.cart{margin-left:14px}

.eyebrow{position:absolute;font-size:6.5px;font-weight:600;color:var(--pink)}
.h-lg{position:absolute;font-weight:600;color:var(--navy);line-height:1.45}
.h-lg em{font-style:normal;color:var(--blue)}
.para{position:absolute;font-size:7px;line-height:1.7;color:var(--muted)}
.btn{position:absolute;height:25px;border-radius:2px;background:var(--navy);color:#fff;font-size:6.5px;font-weight:500;display:flex;align-items:center;justify-content:center}
.btn.ghost{background:#fff;color:var(--muted);border:1px solid #c9ced6}
.photo{position:absolute;border-radius:2px}
.center{text-align:center;left:0;width:712px}

/* hero */
.hero-art{position:absolute;left:337px;top:70px;width:306px;height:260px;background:#f3ede6;border-radius:3px}
.frame{position:absolute;border:5px solid #8a6240;box-shadow:0 3px 8px rgba(0,0,0,.18)}
.badge{position:absolute;left:526px;top:98px;width:137px;height:37px;background:#fff;border-radius:3px;box-shadow:0 2px 8px rgba(0,0,0,.12);padding:5px 8px 0 28px;font-size:6px;color:var(--blue);font-weight:500}
.badge .heart{position:absolute;left:8px;top:11px}
.stars{color:var(--gold);font-size:8px;letter-spacing:1px}
.stars small{color:var(--muted);font-size:5px;letter-spacing:0}

/* steps */
.step-card{position:absolute;width:104px;height:104px;border-radius:3px}
.step-title{position:absolute;font-size:8px;font-weight:500;color:var(--navy);width:140px}
.step-title.hl{color:var(--blue)}
.step-desc{position:absolute;font-size:5.5px;line-height:1.6;color:var(--muted);width:125px}

/* about */
.tint{position:absolute;left:0;width:712px;background:var(--tint)}
.subhead{position:absolute;font-size:8.5px;font-weight:600;color:var(--blue)}
.checks{position:absolute;left:68px;top:1117px;list-style:none;width:265px}
.checks li{position:relative;padding-left:13px;font-size:6.5px;line-height:1.6;color:var(--muted);margin-bottom:10px}
.checks li svg{position:absolute;left:0;top:2px}

/* gallery */
.art-card{position:absolute;width:138px}
.art-card .img{height:168px;background:linear-gradient(#f2f2f2,#e6e4e0);position:relative}
.art-card .img .shelf{position:absolute;left:0;right:0;bottom:0;height:14px;background:#d9d1c6}
.art-card .img .work{position:absolute;left:24px;right:24px;top:70px;bottom:22px;border:3px solid #1b1b1b}
.art-card h4{font-size:7px;font-weight:500;color:var(--navy);margin-top:12px}
.art-card p{font-size:5.5px;line-height:1.6;color:var(--muted);margin-top:3px;height:26px}
.art-card .meta{display:flex;align-items:center;justify-content:space-between}
.art-card .price{font-size:11px;font-weight:600;color:var(--navy)}

/* upload */
.dropzone{position:absolute;left:357px;top:2178px;width:286px;height:293px;background:#f6f8fd;border-radius:3px}
.dropzone .inner{position:absolute;inset:8px;border:1px dashed #9bb6d6;border-radius:2px}

/* cta */
.cta{position:absolute;left:34px;top:2538px;width:643px;height:166px;background:var(--blue);border-radius:4px}

/* categories */
.cat-card{position:absolute;width:139px;height:151px;background:#fff;box-shadow:0 2px 10px rgba(0,0,0,.1);border-radius:2px}
.cat-card .img{position:absolute;left:10px;top:10px;right:10px;height:104px}
.cat-card span{position:absolute;left:0;right:0;top:120px;text-align:center;font-size:6.5px;color:var(--muted)}
.cat-card.active{background:var(--navy)}
.cat-card.active span{color:#fff;top:92px}
.cat-card.active .img{height:76px}
.upload-chip{position:absolute;left:22px;top:110px;width:95px;height:19px;background:#fff;border-radius:2px;font-size:6px;color:var(--navy);display:flex;align-items:center;justify-content:center;gap:4px}

/* testimonials */
.quote{position:absolute;top:3370px;width:184px;height:111px;background:#fff;border-radius:3px;padding:10px}
.quote p{font-size:5.2px;line-height:1.55;color:var(--muted)}
.quote .who{position:absolute;left:12px;top:78px;display:flex;gap:8px;align-items:center}
.quote .avatar{width:24px;height:24px;border-radius:50%;background:linear-gradient(135deg,#6b4a3a,#c4977a)}
.quote .name{font-size:6.5px;color:var(--ink)}
.arrow{position:absolute;top:3415px;width:20px;height:20px;border-radius:50%;border:1.5px solid;display:flex;align-items:center;justify-content:center}

/* footer */
.foot-col{position:absolute;top:3665px;font-size:6.5px;color:var(--muted);line-height:2.2}
.foot-col h5{font-size:8px;font-weight:600;color:var(--navy);line-height:1.6;margin-bottom:2px}
.social{position:absolute;top:3783px;width:9px;height:9px;border-radius:2px}
</style>
</head>
<body>

<!-- board header -->
<div class="board-label" style="left:113px;top:30px;">Landing Page Design</div>
<div class="board-brand"><span class="dot"></span>Brushvello</div>
<div class="board-label" style="left:531px;top:36px;">Colors palette</div>
<div class="swatch" style="left:485px;background:var(--navy)"></div>
<div class="swatch" style="left:568px;background:var(--pink)"></div>
<div class="swatch" style="left:653px;background:var(--blue)"></div>
<div class="board-label" style="left:882px;top:34px;">Font</div>
<div class="font-sample" style="top:89px;">Poppins</div>
<div class="font-sample" style="top:126px;">AaBbCcDdEe</div>
<div class="font-sample" style="top:164px;">1234567890</div>

<main class="page">
  <div class="topbar">
    <div class="contact">
      <span>&#9742; (555) 010-2244</span>
      <span>&#9993; info@brushvellocreations.com</span>
    </div>
    <div class="auth">Login / Sign up</div>
  </div>

  <nav class="nav">
    <div class="logo"><span class="mark"></span>Brushvello Creations</div>
    <ul>
      <li class="active">HOME</li><li>SHOP</li><li>TESTIMONIALS</li><li>OUR STORY</li><li>GALLERY</li><li>FAQS</li>
    </ul>
    <svg class="cart" width="12" height="11" viewBox="0 0 12 11"><path d="M0 1h2l2 6h6l1.5-4.5H3" fill="none" stroke="#555" stroke-width="1"/><circle cx="5" cy="9.5" r="1" fill="#555"/><circle cx="9" cy="9.5" r="1" fill="#555"/><circle cx="10.5" cy="1.5" r="1.5" fill="var(--pink)"/></svg>
  </nav>

  <!-- hero -->
  <h1 class="h-lg" style="left:68px;top:102px;font-size:24px;line-height:36px;width:260px;">Turn Your Digital Photos Into One of a Kind <em>Wall Art</em></h1>
  <p class="para" style="left:68px;top:218px;width:245px;">Experience the beauty of handcrafted art with our digital-to-canvas service. Choose your art style, upload your photo, and receive a stunning, customized artwork that will elevate any space.</p>
  <div class="btn" style="left:68px;top:285px;width:93px;">Get Started</div>
  <div class="btn ghost" style="left:172px;top:285px;width:91px;">Learn more</div>

  <div class="hero-art">
    <div class="frame" style="left:30px;top:42px;width:128px;height:100px;background:linear-gradient(135deg,#c98a4a,#7a4a25);" role="img" aria-label="Framed painting of a dog"></div>
    <div class="frame" style="left:48px;top:152px;width:108px;height:90px;background:linear-gradient(135deg,#f1d6c8,#d9a48f);" role="img" aria-label="Framed painting of a sleeping baby"></div>
    <div class="frame" style="left:170px;top:102px;width:110px;height:82px;background:linear-gradient(135deg,#3f6b35,#b44a3a);" role="img" aria-label="Framed painting of a child among flowers"></div>
  </div>
  <div class="badge">
    <svg class="heart" width="12" height="11" viewBox="0 0 12 11"><path d="M6 10.5S0 6.8 0 3.2A3 3 0 0 1 6 2a3 3 0 0 1 6 1.2C12 6.8 6 10.5 6 10.5z" fill="var(--pink)"/></svg>
    Customers loves us
    <div class="stars">★★★★★ <small>(1200 Reviews)</small></div>
  </div>

  <!-- how it works -->
  <div class="eyebrow center" style="top:400px;">How it Works</div>
  <h2 class="h-lg center" style="top:417px;font-size:17px;line-height:27px;">
    <em>Easy Steps</em> to Transform Your Photos<br>into Artwork
  </h2>
  <p class="para center" style="top:480px;font-size:6.5px;">Turn your cherished memories into beautiful works of art in just a few simple steps. Here's<br>how our service brings your vision to life.</p>

  <svg class="abs" style="left:60px;top:525px;" width="600" height="120" viewBox="0 0 600 120">
    <path d="M5 85 C40 60 60 50 80 40" fill="none" stroke="var(--navy)" stroke-width="1" stroke-dasharray="3 3"/>
    <path d="M140 30 C170 20 190 20 215 25" fill="none" stroke="var(--navy)" stroke-width="1" stroke-dasharray="3 3"/>
    <path d="M295 45 C320 55 340 60 372 65" fill="none" stroke="var(--navy)" stroke-width="1" stroke-dasharray="3 3"/>
    <path d="M450 65 C470 60 490 50 520 40" fill="none" stroke="var(--navy)" stroke-width="1" stroke-dasharray="3 3"/>
    <circle cx="5" cy="85" r="3" fill="var(--navy)"/>
    <circle cx="360" cy="7" r="3" fill="none" stroke="var(--pink)"/>
    <circle cx="415" cy="115" r="2" fill="none" stroke="var(--pink)"/>
    <path d="M585 20 l8 0 l-4 6z" fill="var(--blue)"/>
  </svg>
  <div class="step-card" style="left:70px;top:550px;background:#fce4ec;transform:rotate(-8deg);" role="img" aria-label="Paint palette and brushes illustration"></div>
  <div class="step-card" style="left:225px;top:537px;background:#dde1e7;" role="img" aria-label="Photo upload on a computer screen illustration"></div>
  <div class="step-card" style="left:385px;top:556px;background:#fbfbcf;transform:rotate(-8deg);" role="img" aria-label="Canvas on an easel illustration"></div>
  <div class="step-card" style="left:538px;top:540px;background:#e4f9d4;transform:rotate(-8deg);" role="img" aria-label="Delivery package illustration"></div>

  <div class="step-title" style="left:68px;top:683px;">Choose Your Art Style</div>
  <div class="step-title hl" style="left:223px;top:683px;">Upload Your Photo</div>
  <div class="step-title" style="left:380px;top:683px;">Canvas Customization</div>
  <div class="step-title" style="left:535px;top:683px;">Proofing and Delivery</div>
  <p class="step-desc" style="left:68px;top:702px;">Explore our collection of art styles. Choose the style that best complements your photo and personal taste.</p>
  <p class="step-desc" style="left:223px;top:702px;color:var(--ink);">Upload your digital photo from your device or cloud storage. Our secure upload system ensures your privacy and convenience.</p>
  <p class="step-desc" style="left:380px;top:702px;">Select the ideal canvas size and orientation (horizontal or vertical) for your artwork. We offer a range of sizes to suit any space.</p>
  <p class="step-desc" style="left:535px;top:702px;">Complete the checkout process and within 48 hours, we'll send you a proof of your customized artwork.</p>
  <div class="btn" style="left:259px;top:776px;width:194px;">Create Your Custom Artwork</div>

  <!-- about -->
  <svg class="abs" style="left:0;top:820px;" width="712" height="80" viewBox="0 0 712 80" preserveAspectRatio="none">
    <path d="M0 80 L0 55 C40 48 60 62 95 50 C130 40 150 58 190 44 C230 34 260 52 300 40 C340 30 370 50 410 42 C450 32 480 48 520 38 C560 30 600 46 640 36 C670 30 690 40 712 34 L712 80Z" fill="var(--tint)"/>
  </svg>
  <div class="tint" style="top:880px;height:458px;"></div>
  <div class="eyebrow" style="left:68px;top:956px;">About Us</div>
  <h2 class="h-lg" style="left:68px;top:970px;font-size:16px;line-height:27px;width:300px;">Unleashing Creativity Through Digital Art: <em>Our Story</em></h2>
  <p class="para" style="left:68px;top:1036px;width:220px;font-size:6.5px;">Lorem ipsum dolor sit amet, consectetur adipiscing elit. Sed do eiusmod tempor incididunt ut labore et dolore magna aliqua.</p>
  <div class="subhead" style="left:68px;top:1089px;">Capturing Moments, Creating Art</div>
  <ul class="checks">
    <li><svg width="7" height="6" viewBox="0 0 7 6"><path d="M.5 3l2 2L6.5.5" fill="none" stroke="var(--muted)" stroke-width="1"/></svg>Passionate about turning ordinary photos into extraordinary works of art</li>
    <li style="color:var(--ink)"><svg width="7" height="6" viewBox="0 0 7 6"><path d="M.5 3l2 2L6.5.5" fill="none" stroke="var(--pink)" stroke-width="1"/></svg>Skilled team of artists and designers dedicated to bringing your vision to life</li>
    <li><svg width="7" height="6" viewBox="0 0 7 6"><path d="M.5 3l2 2L6.5.5" fill="none" stroke="var(--muted)" stroke-width="1"/></svg>Utilize state-of-the-art technology and premium materials for museum-quality artwork</li>
    <li><svg width="7" height="6" viewBox="0 0 7 6"><path d="M.5 3l2 2L6.5.5" fill="none" stroke="var(--muted)" stroke-width="1"/></svg>Create customized pieces that evoke the beauty and emotion of traditional paintings</li>
  </ul>
  <div class="btn" style="left:68px;top:1255px;width:93px;">Learn more</div>
  <div class="photo" style="left:373px;top:952px;width:236px;height:291px;background:radial-gradient(circle at 50% 40%,#d9d3cc,#6d5a45 70%,#3e4a2c);" role="img" aria-label="Painted portrait of a merle puppy"></div>
  <div class="photo" style="left:510px;top:1097px;width:164px;height:205px;background:radial-gradient(circle at 50% 40%,#e2ddd5,#7a6650 65%,#44502f);border:3px solid #fff;" role="img" aria-label="Original photo of the same puppy"></div>
  <svg class="abs" style="left:430px;top:1230px;" width="90" height="60" viewBox="0 0 90 60"><path d="M5 5 C0 30 20 50 40 40 C55 32 45 15 35 25 C25 35 40 55 60 50" fill="none" stroke="#19a3b8" stroke-width="1.5"/></svg>

  <!-- gallery -->
  <div class="eyebrow center" style="top:1403px;">Our Gallery</div>
  <h2 class="h-lg center" style="top:1417px;font-size:17px;line-height:27px;">Immerse Yourself in Artistry: Explore<br><em>Our Captivating Gallery</em></h2>
  <p class="para center" style="top:1482px;font-size:6.5px;line-height:1.8;">Discover a world of creativity and inspiration through our diverse collection of<br>captivating artworks. From mesmerizing paintings to thought-provoking sculptures</p>

  <div class="art-card" style="left:68px;top:1539px;"><div class="img"><div class="work" style="background:linear-gradient(135deg,#c98a4a,#6b3f20)" role="img" aria-label="Framed painting of a dog"></div><div class="shelf"></div></div><h4>Ethereal Symphony</h4><p>A captivating blend of colors and forms harmonizing in ethereal beauty</p><div class="meta"><span class="stars">★★★★★ <small>(64)</small></span><span class="price">$80</span></div></div>
  <div class="art-card" style="left:214px;top:1539px;"><div class="img"><div class="work" style="background:linear-gradient(135deg,#3f6b35,#b44a3a)" role="img" aria-label="Framed painting of a child in a garden"></div><div class="shelf"></div></div><h4>Whispering Dreams</h4><p>Delicate strokes unveil a dreamscape, where whispers of imagination come alive.</p><div class="meta"><span class="stars">★★★★★ <small>(64)</small></span><span class="price">$80</span></div></div>
  <div class="art-card" style="left:360px;top:1539px;"><div class="img"><div class="work" style="left:40px;right:40px;top:58px;background:linear-gradient(135deg,#c4bcb2,#4d5b38)" role="img" aria-label="Framed painting of a puppy"></div><div class="shelf"></div></div><h4>Enchanted Reverie</h4><p>Journey into a realm of enchantment, where reveries dance with enchanting hues.</p><div class="meta"><span class="stars">★★★★★ <small>(64)</small></span><span class="price">$80</span></div></div>
  <div class="art-card" style="left:505px;top:1539px;"><div class="img"><div class="work" style="background:linear-gradient(135deg,#f1d6c8,#d29c86)" role="img" aria-label="Framed painting of a sleeping baby"></div><div class="shelf"></div></div><h4>Serenity Unveiled</h4><p>Serene brushstrokes reveal a tranquil oasis, inviting inner peace and solace.</p><div class="meta"><span class="stars">★★★★★ <small>(64)</small></span><span class="price">$80</span></div></div>

  <div class="art-card" style="left:68px;top:1801px;"><div class="img"><div class="work" style="background:linear-gradient(135deg,#6f9a4d,#9ab7c9)" role="img" aria-label="Framed painting of a grandparent and child"></div><div class="shelf"></div></div><h4>Enigma of Reflections</h4><p>Layers of reflections weave an enigmatic tale, inviting contemplation and intrigue.</p><div class="meta"><span class="stars">★★★★★ <small>(64)</small></span><span class="price">$80</span></div></div>
  <div class="art-card" style="left:214px;top:1801px;"><div class="img"><div class="work" style="left:40px;right:40px;top:58px;background:linear-gradient(135deg,#c4bcb2,#5a4a35)" role="img" aria-label="Framed painting of a puppy"></div><div class="shelf"></div></div><h4>Harmony of Colors</h4><p>Vibrant colors intertwine, creating a harmonious symphony of visual delight.</p><div class="meta"><span class="stars">★★★★★ <small>(64)</small></span><span class="price">$80</span></div></div>
  <div class="art-card" style="left:360px;top:1801px;"><div class="img"><div class="work" style="background:linear-gradient(135deg,#5a7a8c,#3e5b36)" role="img" aria-label="Framed painting of a couple walking"></div><div class="shelf"></div></div><h4>Celestial Cascade</h4><p>Celestial hues cascade, unveiling a cosmic dance of light and wonder.</p><div class="meta"><span class="stars">★★★★★ <small>(64)</small></span><span class="price">$80</span></div></div>
  <div class="art-card" style="left:505px;top:1801px;"><div class="img"><div class="work" style="background:linear-gradient(135deg,#3f6b35,#a8442f)" role="img" aria-label="Framed painting of a child among flowers"></div><div class="shelf"></div></div><h4>Mystic Melodies</h4><p>Abstract rhythms of colors and lines, evoking a sense of mysterious melodies.</p><div class="meta"><span class="stars">★★★★★ <small>(64)</small></span><span class="price">$80</span></div></div>
  <div class="btn" style="left:269px;top:2077px;width:174px;">Discover Our Art Gallery</div>

  <!-- upload -->
  <div class="eyebrow" style="left:68px;top:2212px;">Upload Your Image</div>
  <h2 class="h-lg" style="left:68px;top:2226px;font-size:17px;line-height:27px;"><em>Transform</em> Your Image<br>into <em>Art</em></h2>
  <p class="para" style="left:68px;top:2290px;width:262px;font-size:6.5px;line-height:1.75;">Are you looking to transform your favorite image into a stunning piece of art? Our custom artwork service allows you to bring your vision to life. Whether it's a cherished photograph, a digital design, or an illustration, our talented artists will create a unique masterpiece that captures the essence of your image. With our easy-to-use upload feature, you can conveniently submit your image and watch it undergo a mesmerizing artistic transformation.</p>
  <div class="btn" style="left:68px;top:2419px;width:153px;">Get Your Masterpiece Now</div>
  <div class="dropzone"><div class="inner"></div>
    <svg class="abs" style="left:118px;top:82px;" width="52" height="62" viewBox="0 0 52 62">
      <path d="M10 26a10 10 0 0 1 4-19 13 13 0 0 1 25 3 8 8 0 0 1 3 16z" fill="#6fb6e6"/>
      <rect x="10" y="14" width="26" height="34" rx="2" fill="#fff" stroke="#c7d6e6"/>
      <path d="M15 22h16M15 27h16M15 32h12" stroke="#c7d6e6" stroke-width="1.5"/>
      <circle cx="35" cy="46" r="10" fill="#f5b90a"/>
      <path d="M35 51v-9M31 45l4-4 4 4" fill="none" stroke="var(--blue)" stroke-width="2"/>
    </svg>
    <div class="abs" style="left:0;right:0;top:187px;text-align:center;font-size:9px;font-weight:500;color:var(--navy);">Drop Your Files Here, or <span style="color:var(--blue)">Browse</span></div>
    <div class="abs" style="left:0;right:0;top:206px;text-align:center;font-size:5.5px;color:var(--muted);">Supported file types: JPG, PNG, RAW. Maximum file size: 10MB</div>
  </div>

  <!-- cta -->
  <div class="cta"></div>
  <h2 class="h-lg" style="left:68px;top:2554px;font-size:17px;line-height:28px;color:#fff;width:340px;">Unlock Your Creativity with Brushvello Creations Art!</h2>
  <p class="para" style="left:68px;top:2622px;width:300px;color:#e6f0fa;font-size:6.5px;">Join our vibrant community of art enthusiasts and embark on a journey of artistic exploration and growth. Start creating masterpieces today!</p>
  <div class="btn" style="left:68px;top:2661px;width:82px;">Get Started</div>
  <div class="photo" style="left:397px;top:2603px;width:75px;height:124px;background:linear-gradient(160deg,#7a5a45,#e9e3d6 60%,#7d8f5a);" role="img" aria-label="Photo of a bride holding a bouquet"></div>
  <div class="photo" style="left:481px;top:2561px;width:79px;height:120px;background:linear-gradient(160deg,#9dbfd3,#e5e0d9 55%,#6f9a4d);" role="img" aria-label="Photo of a grandmother with her grandchild"></div>
  <div class="photo" style="left:566px;top:2518px;width:77px;height:121px;background:linear-gradient(160deg,#3f6b35,#b44a3a 60%,#4a5f2d);" role="img" aria-label="Photo of a child among flowers"></div>

  <!-- categories -->
  <div class="cat-card" style="left:68px;top:2768px;"><div class="img" style="background:radial-gradient(circle at 50% 40%,#d9d3cc,#6d5a45 70%,#44502f);" role="img" aria-label="Oil painting of a puppy"></div><span>Oil Painting</span></div>
  <div class="cat-card active" style="left:223px;top:2768px;"><div class="img" style="background:linear-gradient(135deg,#f3dccf,#d29c86);" role="img" aria-label="Oil painting of a sleeping baby"></div><span>Oil Painting</span>
    <div class="upload-chip">Upload Image <svg width="7" height="7" viewBox="0 0 7 7"><path d="M3.5 5V1M1.5 3l2-2 2 2M.5 6.5h6" fill="none" stroke="var(--navy)" stroke-width=".8"/></svg></div></div>
  <div class="cat-card" style="left:68px;top:2932px;"><div class="img" style="background:linear-gradient(160deg,#7a5a45,#e9e3d6 60%,#6f8050);" role="img" aria-label="Oil painting of a bride with a bouquet"></div><span>Oil Painting</span></div>
  <div class="cat-card" style="left:223px;top:2932px;"><div class="img" style="background:linear-gradient(160deg,#9dbfd3,#e5e0d9 55%,#6f9a4d);" role="img" aria-label="Oil painting of a grandmother and grandchild"></div><span>Oil Painting</span></div>

  <div class="eyebrow" style="left:388px;top:2800px;">Categories</div>
  <h2 class="h-lg" style="left:388px;top:2816px;font-size:17px;line-height:28px;">Choose Your <em>Favorite Style</em><br>and We'll do the Rest</h2>
  <p class="para" style="left:388px;top:2884px;width:258px;font-size:6.5px;line-height:1.75;">Are you looking to transform your favorite image into a stunning piece of art? Our custom artwork service allows you to bring your vision to life. Whether it's a cherished photograph, a digital design, or an illustration, our talented artists will create a unique masterpiece that captures the essence of your image. With our easy-to-use upload feature, you can conveniently submit your image and watch it undergo a mesmerizing artistic transformation.</p>
  <div class="btn" style="left:388px;top:3011px;width:153px;">Get Your Masterpiece Now</div>

  <!-- testimonials -->
  <svg class="abs" style="left:0;top:3130px;" width="712" height="70" viewBox="0 0 712 70" preserveAspectRatio="none">
    <path d="M0 70 L0 45 C40 38 70 52 110 40 C150 30 180 48 220 36 C260 26 300 44 340 34 C380 26 410 42 450 32 C490 24 520 40 560 30 C600 22 640 36 680 28 L712 26 L712 70Z" fill="var(--tint)"/>
  </svg>
  <div class="tint" style="top:3195px;height:383px;"></div>
  <div class="eyebrow center" style="top:3233px;">Testimonials</div>
  <h2 class="h-lg center" style="top:3247px;font-size:17px;line-height:28px;">Hear What <em>Our Clients</em> Say About Our<br>Artworks</h2>
  <p class="para center" style="top:3313px;font-size:6.5px;line-height:1.8;">Discover why our clients rave about their experience with Brushvello Creations. Read their<br>heartfelt testimonials and see how our artwork has made a lasting impact on their lives.</p>

  <div class="arrow" style="left:26px;border-color:#c4c9d6;"><svg width="8" height="8" viewBox="0 0 8 8"><path d="M7 4H1M4 1L1 4l3 3" fill="none" stroke="#c4c9d6" stroke-width="1.2"/></svg></div>
  <div class="arrow" style="left:666px;border-color:var(--pink);"><svg width="8" height="8" viewBox="0 0 8 8"><path d="M1 4h6M4 1l3 3-3 3" fill="none" stroke="var(--pink)" stroke-width="1.2"/></svg></div>

  <div class="quote" style="left:68px;"><p>I couldn't be happier with the artwork created by Brushvello Creations. The attention to detail and the level of craftsmanship is truly remarkable. It has exceeded all my expectations and has become the focal point of my living room.</p>
    <div class="who"><div class="avatar" role="img" aria-label="Customer portrait"></div><div><div class="name">Daniel Whitmore</div><div class="stars">★★★★★</div></div></div></div>
  <div class="quote" style="left:264px;"><p>I recently commissioned Brushvello Creations to create a custom artwork for my husband's birthday, and it was blown away by the result. The team captured his personality and interests perfectly, and the final piece left him speechless.</p>
    <div class="who"><div class="avatar" role="img" aria-label="Customer portrait"></div><div><div class="name">Rosalind</div><div class="stars">★★★★★</div></div></div></div>
  <div class="quote" style="left:459px;"><p>I discovered Brushvello Creations while searching for new inspiration and I'm so glad I did. The artwork I purchased for my office has transformed the space and evokes a sense of inspiration every time I walk in. The quality of the piece is outstanding.</p>
    <div class="who"><div class="avatar" role="img" aria-label="Customer portrait"></div><div><div class="name">Clara Penfield</div><div class="stars">★★★★★</div></div></div></div>
  <svg class="abs" style="left:336px;top:3508px;" width="40" height="6" viewBox="0 0 40 6"><circle cx="3" cy="3" r="2" fill="#c4c9d6"/><circle cx="12" cy="3" r="2" fill="#c4c9d6"/><circle cx="21" cy="3" r="2" fill="#c4c9d6"/><circle cx="30" cy="3" r="2" fill="#c4c9d6"/><circle cx="38" cy="3" r="2" fill="#c4c9d6"/></svg>

  <!-- footer -->
  <div class="tint" style="top:3617px;height:238px;background:#eceefb;"></div>
  <div class="logo" style="position:absolute;left:72px;top:3657px;font-size:13px;"><span class="mark"></span>Brushvello Creations</div>
  <p class="para" style="left:72px;top:3702px;width:200px;font-size:6px;">Experience the beauty of handcrafted art with our digital-to-canvas service. Choose your art style, upload your photo, and receive a stunning, customized artwork that will elevate any space.</p>
  <div class="foot-col" style="left:319px;"><h5>Company</h5>Home<br>Testimonials<br>Our Story<br>FAQs</div>
  <div class="foot-col" style="left:407px;"><h5>Explore</h5>Categories<br>Gallery<br>Offers<br>About Us</div>
  <div class="foot-col" style="left:488px;"><h5>Contact Us</h5>
    <span style="color:var(--pink)">&#9993;</span> support@brushvellomart.com<br>
    <span style="color:var(--pink)">&#9993;</span> hello@brushvellomart.com<br>
    <span style="color:var(--blue)">&#9742;</span> (555) 010-2244<br>
    <span style="color:var(--blue)">&#9679;</span> 48 Harbor Lane Fairview, USA 10482</div>
  <div class="abs" style="left:72px;top:3762px;font-size:7.5px;font-weight:600;color:var(--navy);">Follow Us</div>
  <div class="social" style="left:72px;background:var(--pink);"></div>
  <div class="social" style="left:86px;background:#8fa6c4;border-radius:50%;"></div>
  <div class="social" style="left:100px;background:#8fa6c4;border-radius:50%;"></div>
  <div class="abs" style="left:225px;top:3766px;width:418px;height:1px;background:#c9cfe0;"></div>
  <div class="abs" style="left:225px;top:3783px;font-size:5.5px;color:var(--muted);">Privacy Policy &bull; Terms and Conditions</div>
  <div class="abs" style="left:392px;top:3783px;font-size:5.5px;color:var(--muted);">All artwork and content &copy; 2023 Brushvello Creations Art. All rights reserved.</div>
</main>
</body>
</html>
```